BRIGHTDESK COWORKING Website design and coding

BRIGHTDESK COWORKING

BRIGHTDESK is Galveston’s first (and currently only) shared business co-working space. We share the same upscale, casual work environment, but we work independently on our own (or our team’s) projects and goals. For only a flat $195 membership fee per month, you have your very own all-inclusive, fun, personal business office environment. Website is written (Word file #12, below); and all pictures etc provided. Galveston is a beachy, coastal, historic city an hour from Houston, Texas USA. Logo (file 11 below) is temporary only.

Target Market(s)

Outside sales people, medical students looking for study hall, Houston companies looking for local office, real estate agents, graphic artists, entrepreneurs, etc

Contact Information for Business Card

will discuss --want to combine with current business card with multiple businesses

Logo Text

BRIGHTDESK COWORKING

Coding

Coded - Design and coding required

Number of Pages Required

5+ page

Colors
ec1f27
fbed22

Requirements
Nice to have
• maroon/wine dominant with yellow and red accents, gray base are the colors of the space--website could coordinate--but open to creative ideas/combinations

```html
<!DOCTYPE html>
<html lang="en">
<head>
<meta charset="utf-8">
<title>BRIGHTDESK COWORKING</title>
<link href="https://fonts.googleapis.com/css2?family=Bebas+Neue&family=Montserrat:wght@400;500;600;700&display=swap" rel="stylesheet">
<style>
:root{
  --red:#ec1f27;
  --yellow:#fbed22;
  --dark:#1b1b1b;
  --footer:#161616;
  --gray:#f2f2f2;
  --text:#4a4a4a;
  --heading:#2a2a2a;
  --white:#ffffff;
}
*{margin:0;padding:0;box-sizing:border-box}
html,body{width:1200px;height:4713px;overflow:hidden}
body{position:relative;background:var(--white);font-family:'Montserrat',sans-serif;color:var(--text);font-size:11.5px;line-height:1.7}
.abs{position:absolute}
.heading{font-family:'Bebas Neue',sans-serif;color:var(--heading);font-size:36px;letter-spacing:2px;text-align:center;font-weight:400;line-height:1}
.btn{position:absolute;display:flex;align-items:center;justify-content:center;background:var(--red);color:var(--white);border-radius:20px;font-size:12px;font-weight:500}
.photo{position:absolute}
.accent{position:absolute;width:40px;height:35px;background:var(--yellow)}
.hero{position:absolute;left:0;top:0;width:1200px;height:714px;background:linear-gradient(180deg,#2c2620 0%,#3b3126 35%,#5a4323 65%,#2b2219 100%)}
.hero-shade{position:absolute;inset:0;background:radial-gradient(ellipse at 30% 60%,rgba(190,140,60,.35),transparent 60%),radial-gradient(ellipse at 85% 70%,rgba(40,80,40,.35),transparent 55%)}
.logo{position:absolute;display:flex;align-items:center;gap:10px}
.logo-mark{width:26px;height:26px;background:var(--red)}
.logo-text{font-family:'Montserrat',sans-serif;font-weight:700;color:var(--yellow);line-height:1.05;letter-spacing:.5px}
.nav{position:absolute;left:439px;top:78px;font-size:12.5px;color:#e8e8e8}
.nav a{position:absolute;white-space:nowrap;text-decoration:none;color:#e8e8e8}
.nav a.active{color:var(--yellow)}
.call{position:absolute;left:823px;top:26px;display:flex;align-items:center;gap:8px;color:var(--white);font-size:11px;line-height:1.15}
.call-icon{width:32px;height:32px;border-radius:50%;background:var(--yellow);display:flex;align-items:center;justify-content:center}
.hero-title{position:absolute;left:0;width:1200px;top:328px;text-align:center;font-family:'Bebas Neue',sans-serif;color:var(--white);font-size:31px;letter-spacing:7px;line-height:37px}
.slide-dots{position:absolute;left:26px;top:340px;color:var(--yellow);font-size:12px}
.about-title{top:800px}
.underline{position:absolute;left:562px;top:867px;width:62px;height:4px;background:var(--red)}
.subhead{font-family:'Bebas Neue',sans-serif;font-size:29px;color:var(--heading);letter-spacing:1.5px;line-height:1}
.about-copy{font-size:11.5px;line-height:18px}
.about-copy p{margin-bottom:14px}
.band-gray{position:absolute;left:0;width:1200px;background:var(--gray)}
.list{position:absolute;list-style:none}
.list li{position:relative;padding-left:26px}
.tick{position:absolute;left:0;width:17px;height:17px}
.focus{position:absolute}
.philosophy{position:absolute;left:0;top:3416px;width:1200px;height:441px;background:linear-gradient(180deg,#2a2a27 0%,#1c1c1a 60%,#262620 100%)}
.card{position:absolute;top:3599px;height:258px;text-align:center;padding:0 26px;font-size:10.8px;line-height:1.65}
.card h3{font-family:'Bebas Neue',sans-serif;font-weight:400;font-size:17px;letter-spacing:1.6px;margin-bottom:18px}
.card-light{background:var(--white);color:var(--text)}
.card-light h3{color:var(--heading);margin-top:70px}
.card-red{background:var(--red);color:var(--white)}
.card-red h3{color:var(--white);margin-top:52px}
.field{position:absolute;border:1px solid #cfcfcf;background:var(--white);font-size:10.5px;color:#999;padding:8px 14px}
.footer{position:absolute;left:0;top:4302px;width:1200px;height:346px;background:var(--footer);color:#d8d8d8;font-size:12px}
.fcol h4{font-family:'Bebas Neue',sans-serif;font-weight:400;color:var(--white);font-size:17px;letter-spacing:1.4px;line-height:1}
.fcol .rule{width:36px;height:2px;background:var(--white);margin:8px 0 10px}
.fcol ul{list-style:none}
.fcol ul li{line-height:22.4px}
.fcol ul li::before{content:"•";margin-right:8px;color:var(--white)}
.fcol .line{line-height:24px}
.social{position:absolute;width:30px;height:30px;border-radius:50%;background:#3a3a3a}
.social.first{background:var(--red)}
.copyright{position:absolute;left:73px;top:4668px;font-size:11px;color:#555}
.pay{position:absolute;top:4663px;width:36px;height:25px;border-radius:3px}
</style>
</head>
<body>
<svg width="0" height="0" class="abs" aria-hidden="true">
  <symbol id="tick" viewBox="0 0 20 20"><circle cx="10" cy="10" r="8.4" fill="none" stroke="#333" stroke-width="1.6"/><path d="M6 10.3l2.7 2.7L14.3 7" fill="none" stroke="#333" stroke-width="1.8" stroke-linecap="round" stroke-linejoin="round"/></symbol>
</svg>

<!-- HEADER / HERO -->
<section class="hero" role="img" aria-label="Photo of the coworking space interior with desks, lockers and plants">
  <div class="hero-shade"></div>
</section>
<svg class="abs" style="left:560px;top:712px" width="80" height="26" viewBox="0 0 80 26" aria-hidden="true"><path d="M0 0 H80 C62 0 56 24 40 24 C24 24 18 0 0 0Z" fill="#2b2219"/></svg>

<div class="logo" style="left:58px;top:42px">
  <div class="logo-mark"></div>
  <div class="logo-text" style="font-size:18px">BRIGHTDESK<br>COWORKING</div>
</div>

<div class="call">
  <div class="call-icon"><svg width="16" height="16" viewBox="0 0 24 24"><path d="M6.6 10.8a15.1 15.1 0 0 0 6.6 6.6l2.2-2.2c.3-.3.7-.4 1-.2 1.1.4 2.3.6 3.6.6.6 0 1 .4 1 1V20c0 .6-.4 1-1 1A17 17 0 0 1 3 4c0-.6.4-1 1-1h3.5c.6 0 1 .4 1 1 0 1.3.2 2.5.6 3.6.1.3 0 .7-.2 1z" fill="#1b1b1b"/></svg></div>
  <div><b>Call us</b><br>555 014 2290</div>
</div>
<div class="btn" style="left:982px;top:24px;width:139px;height:33px;font-size:13px">Get A Quote</div>

<nav class="nav">
  <svg class="abs" style="left:15px;top:-16px" width="10" height="10" viewBox="0 0 10 10"><path d="M5 0L10 5L5 10L0 5Z" fill="#fbed22"/></svg>
  <a class="active" style="left:0">Home</a>
  <span class="abs" style="left:0;top:22px;width:40px;height:2px;background:var(--yellow)"></span>
  <a style="left:77px">About</a>
  <a style="left:150px">Amenities</a>
  <a style="left:247px">Membership</a>
  <a style="left:362px">Gallery</a>
  <a style="left:441px">The Brightdesk Philosophy</a>
  <a style="left:631px">Contact</a>
</nav>

<div class="slide-dots">
  <span class="abs" style="left:0;top:0;width:6px;height:6px;background:var(--yellow)"></span>
  <span class="abs" style="left:0;top:11px;width:20px;height:2px;background:var(--yellow)"></span>
  <span class="abs" style="left:34px;top:2px">02</span>
  <span class="abs" style="left:0;top:24px;width:6px;height:6px;background:var(--yellow)"></span>
</div>

<h1 class="hero-title" style="font-weight:400">CO-WORKING SPACE<br>FOR A SUCCESS</h1>

<svg class="abs" style="left:590px;top:668px" width="20" height="44" viewBox="0 0 20 44" aria-hidden="true"><path d="M10 0V40M3 33l7 8 7-8" fill="none" stroke="#fff" stroke-width="1.8"/></svg>

<!-- ABOUT -->
<h2 class="heading abs about-title" style="left:0;width:1200px">ABOUT US</h2>
<div class="underline"></div>

<div class="photo" style="left:269px;top:924px;width:435px;height:353px;clip-path:polygon(0 0,100% 0,100% 93%,28% 93%,28% 100%,0 100%);background:linear-gradient(135deg,#8a6a46,#4d3a2a 50%,#2a2320)" role="img" aria-label="Photo of the lounge with leather sofas and a glass-walled office"></div>
<div class="photo" style="left:112px;top:864px;width:334px;height:225px;background:linear-gradient(160deg,#d9d3c4,#9c8a66 45%,#3a3128)" role="img" aria-label="Photo of the open workspace with pendant lamps and black-and-yellow chairs"></div>
<div class="accent" style="left:459px;top:875px"></div>
<div class="accent" style="left:210px;top:1107px"></div>

<div class="abs" style="left:745px;top:952px;width:350px">
  <h3 class="subhead" style="font-weight:400">BRIGHTDESK COWORKING</h3>
  <div class="about-copy" style="margin-top:24px">
    <p>BRIGHTDESK is Galveston’s first (and currently only) shared business co-working space. We share the same upscale, casual work environment, but we work independently on our own (or our team’s) projects and goals.</p>
    <p>For only a flat $195 membership fee per month, you have your very own all-inclusive, fun, personal business office environment.</p>
  </div>
</div>
<div class="btn" style="left:739px;top:1162px;width:161px;height:33px">Read More</div>

<!-- AMENITIES -->
<section class="band-gray" style="top:1349px;height:686px"></section>
<h2 class="heading abs" style="left:0;width:1200px;top:1410px">AMENITIES</h2>
<p class="abs" style="left:0;width:1200px;top:1452px;text-align:center;line-height:18px">BRIGHTDESK is the first Galveston co-working space, and offers all of the following features,<br>all included in your monthly $195 membership fee</p>

<ul class="list" style="left:110px;top:1557px;width:400px;line-height:22.4px">
  <li><svg class="tick" style="top:2px"><use href="#tick"/></svg>Open office or a private cubicle for your daily use.</li>
  <li><svg class="tick" style="top:2px"><use href="#tick"/></svg>Free Wifi.</li>
  <li><svg class="tick" style="top:2px"><use href="#tick"/></svg>24 hour access.</li>
  <li><svg class="tick" style="top:2px"><use href="#tick"/></svg>Comfortable open casual spaces or private office cubicles – at your option.</li>
  <li><svg class="tick" style="top:2px"><use href="#tick"/></svg>Communal coffee bar and kitchen, with FREE coffee.</li>
  <li><svg class="tick" style="top:2px"><use href="#tick"/></svg>Health and social distance amenities, including hand washing stations, and distanced desks with glass or wall separations, rigorous cleaning and sanitizing schedules.</li>
  <li><svg class="tick" style="top:2px"><use href="#tick"/></svg>Use of copier/printer (at per-copy cost).</li>
  <li><svg class="tick" style="top:2px"><use href="#tick"/></svg>Great modern design – a place that looks “cutting edge” and which you will be proud to call your own.</li>
  <li><svg class="tick" style="top:2px"><use href="#tick"/></svg>Keyless, digital door entry.</li>
  <li><svg class="tick" style="top:2px"><use href="#tick"/></svg>Mail service.</li>
</ul>
<div class="btn" style="left:112px;top:1896px;width:161px;height:33px">Read More</div>

<div class="photo" style="left:789px;top:1521px;width:335px;height:225px;background:linear-gradient(160deg,#cfcbc2,#8d8578 55%,#4a4036)" role="img" aria-label="Photo of pendant lamps over the workspace ceiling"></div>
<div class="photo" style="left:531px;top:1581px;width:435px;height:355px;clip-path:polygon(0 0,100% 0,100% 100%,55% 100%,55% 85%,0 85%);background:linear-gradient(150deg,#a89a84,#c9a56a 40%,#6b5332 75%,#3a2e22)" role="img" aria-label="Photo of long wooden desks with yellow-and-black chairs"></div>
<div class="accent" style="left:979px;top:1760px"></div>

<!-- MEMBERSHIP -->
<h2 class="heading abs" style="left:0;width:1220px;top:2175px">MEMBERSHIP</h2>
<div class="photo" style="left:112px;top:2204px;width:261px;height:255px;background:linear-gradient(160deg,#d8d4cc,#a9a398 60%,#6a645b)" role="img" aria-label="Photo of the entrance wall with lockers"></div>
<div class="photo" style="left:234px;top:2274px;width:340px;height:405px;clip-path:polygon(0 0,100% 0,100% 87%,43% 87%,43% 100%,0 100%);background:linear-gradient(160deg,#b8b1a6,#5b524c 50%,#1f1c1c)" role="img" aria-label="Photo of the lounge with black leather sofas, red lockers and dark tile floor"></div>
<div class="accent" style="left:179px;top:2474px"></div>

<ul class="list" style="left:624px;top:2268px;width:470px;line-height:22px">
  <li style="padding-left:40px;margin-bottom:22px"><svg class="tick" style="top:2px"><use href="#tick"/></svg>For only $195 a month, charged to your credit card, you get the all-inclusive amenities listed above, for one flat fee. The only “extras” are for copies, on a per-copy basis.</li>
  <li style="padding-left:40px;margin-bottom:22px"><svg class="tick" style="top:2px"><use href="#tick"/></svg>WiFi, coffee, use of the conference room, office use, use of the kitchen and all the other features listed under “AMENITIES” above, are INCLUDED at no additional cost.</li>
  <li style="padding-left:40px;margin-bottom:22px"><svg class="tick" style="top:2px"><use href="#tick"/></svg>Get a FREE day, to try us out by emailing us at the link here (link).</li>
  <li style="padding-left:40px;margin-bottom:22px"><svg class="tick" style="top:2px"><use href="#tick"/></svg>(Need to make an email form that requests name, address, phone, email and description of business).</li>
  <li style="padding-left:40px"><svg class="tick" style="top:2px"><use href="#tick"/></svg>We’ll call you back with a “smart lock” code and you’re in!</li>
</ul>
<div class="btn" style="left:650px;top:2615px;width:159px;height:33px">Read More</div>

<!-- GALLERY -->
<section class="band-gray" style="top:2728px;height:688px"></section>
<h2 class="heading abs" style="left:0;width:1196px;top:2782px">GALLERY</h2>
<div class="photo" style="left:73px;top:2849px;width:333px;height:212px;background:linear-gradient(120deg,#c9c3b6,#e6e3dc 50%,#8a7f70)" role="img" aria-label="Photo of a hallway with a printer station"></div>
<div class="photo" style="left:426px;top:2849px;width:341px;height:448px;background:linear-gradient(170deg,#6b665f,#2d2a27 45%,#151413)" role="img" aria-label="Photo of the coffee bar with dark stools"></div>
<svg class="focus" style="left:582px;top:3054px" width="30" height="30" viewBox="0 0 30 30" aria-hidden="true"><path d="M2 9V2h7M21 2h7v7M28 21v7h-7M9 28H2v-7" fill="none" stroke="#fff" stroke-width="2.2"/><rect x="9" y="9" width="12" height="12" fill="none" stroke="#fff" stroke-width="2"/></svg>
<div class="photo" style="left:787px;top:2849px;width:335px;height:212px;background:linear-gradient(150deg,#7a6a58,#c9a582 50%,#5c4b3a)" role="img" aria-label="Photo of a potted plant on the kitchen counter"></div>
<div class="photo" style="left:73px;top:3085px;width:333px;height:212px;background:linear-gradient(160deg,#b3a58a,#c69c55 50%,#4e3c28)" role="img" aria-label="Photo of a break room with wooden tables"></div>
<div class="photo" style="left:787px;top:3085px;width:335px;height:212px;background:linear-gradient(150deg,#d0ccc2,#8f7558 55%,#4a3b2e)" role="img" aria-label="Photo of the kitchen island with stools"></div>
<div class="btn" style="left:514px;top:3330px;width:159px;height:33px">View More</div>

<!-- PHILOSOPHY -->
<section class="philosophy" role="img" aria-label="Dimmed photo of the workspace behind the philosophy section"></section>
<h2 class="heading abs" style="left:0;width:1210px;top:3530px;color:var(--white)">THE BRIGHTDESK PHILOSOPHY</h2>

<article class="card card-light" style="left:73px;width:335px">
  <h3>WORK OUTSIDE THE HOME</h3>
  <p>Free yourself for the burdens of house or school, and work in an environment that MOTIVATES you instead of DISTRACTS you.Meet like-minded people that can help you along, and yet you have the option to work in a quiet-and very comfortable</p>
</article>
<article class="card card-red" style="left:432px;width:335px">
  <h3>BRIGHTDESK THE COMPETITION</h3>
  <p>Free yourself for the burdens of house or school, and work in an environment that MOTIVATES you instead of DISTRACTS you.Meet like-minded people that can help you along, and yet you have the option to work in a quiet-and very comfortable</p>
  <p style="margin-top:20px;font-size:12px">Read More <svg width="16" height="16" viewBox="0 0 16 16" style="vertical-align:-3px"><circle cx="8" cy="8" r="6.8" fill="none" stroke="#fff" stroke-width="1.2"/><path d="M4.5 8h6M8 5.5L10.5 8 8 10.5" fill="none" stroke="#fff" stroke-width="1.2"/></svg></p>
</article>
<article class="card card-light" style="left:789px;width:335px">
  <h3>WORK IT OUT WITH YOUR COWORKERS</h3>
  <p>Free yourself for the burdens of house or school, and work in an environment that MOTIVATES you instead of DISTRACTS you.Meet like-minded people that can help you along, and yet you have the option to work in a quiet-and very comfortable</p>
</article>
<svg class="abs" style="left:22px;top:3722px" width="28" height="28" viewBox="0 0 28 28" aria-label="Previous"><circle cx="14" cy="14" r="12.5" fill="none" stroke="#fff" stroke-width="1.5"/><path d="M20 14H8M12.5 9.5L8 14l4.5 4.5" fill="none" stroke="#fff" stroke-width="1.5"/></svg>
<svg class="abs" style="left:1146px;top:3722px" width="28" height="28" viewBox="0 0 28 28" aria-label="Next"><circle cx="14" cy="14" r="12.5" fill="none" stroke="#fff" stroke-width="1.5"/><path d="M8 14h12M15.5 9.5L20 14l-4.5 4.5" fill="none" stroke="#fff" stroke-width="1.5"/></svg>

<!-- QUICK CONTACT -->
<div class="abs" style="left:1005px;top:3915px;width:340px;height:340px;border-radius:50%;background:#f4f7fb"></div>
<h2 class="heading abs" style="left:0;width:1200px;top:3945px">QUICK CONTACT</h2>
<div class="field" style="left:349px;top:4013px;width:242px;height:42px">Name*</div>
<div class="field" style="left:349px;top:4073px;width:242px;height:42px">Email*</div>
<div class="field" style="left:349px;top:4135px;width:242px;height:42px">Phone*</div>
<div class="field" style="left:611px;top:4013px;width:242px;height:164px">Message</div>
<div class="btn" style="left:514px;top:4209px;width:159px;height:33px">Send</div>

<!-- FOOTER -->
<footer class="footer">
  <div class="logo" style="left:77px;top:122px">
    <div class="logo-mark" style="width:40px;height:40px"></div>
    <div class="logo-text" style="font-size:27px">BRIGHTDESK<br>COWORKING</div>
  </div>

  <div class="fcol abs" style="left:419px;top:73px">
    <h4>QUICK LINK</h4>
    <div class="rule"></div>
    <ul>
      <li style="color:var(--yellow)">Home</li>
      <li>About</li>
      <li>Amenities</li>
      <li>Membership</li>
      <li>Gallery</li>
      <li>Philosophy</li>
      <li>Contact</li>
    </ul>
  </div>

  <div class="fcol abs" style="left:589px;top:73px;width:230px">
    <h4>PHYSICAL LOCATION</h4>
    <div class="rule"></div>
    <div class="line" style="padding-left:26px;position:relative">
      <svg class="abs" style="left:0;top:5px" width="12" height="14" viewBox="0 0 12 16"><path d="M6 1a4.6 4.6 0 0 0-4.6 4.6C1.4 9.5 6 15 6 15s4.6-5.5 4.6-9.4A4.6 4.6 0 0 0 6 1z" fill="none" stroke="#ddd" stroke-width="1.3"/><circle cx="6" cy="5.7" r="1.6" fill="#ddd"/></svg>
      BRIGHTDESK COWORKING<br>418 Harbor Lane, Suite 12<br>Galveston, TX 77501
    </div>
    <div class="line" style="margin-top:24px;padding-left:26px;position:relative">
      <svg class="abs" style="left:0;top:6px" width="13" height="12" viewBox="0 0 13 12"><rect x="1" y="2" width="11" height="9" rx="1" fill="none" stroke="#ddd" stroke-width="1.2"/><path d="M3 2V1h7v1M3 6h7" stroke="#ddd" stroke-width="1.2"/></svg>
      409-555-0187
    </div>
    <div class="line" style="padding-left:26px;position:relative">
      <svg class="abs" style="left:0;top:7px" width="13" height="10" viewBox="0 0 13 10"><rect x=".6" y=".6" width="11.8" height="8.8" fill="none" stroke="#ddd" stroke-width="1.2"/><path d="M.6.6l5.9 5 5.9-5" fill="none" stroke="#ddd" stroke-width="1.2"/></svg>
      hello@brightdeskcowork.com
    </div>
  </div>

  <div class="fcol abs" style="left:849px;top:73px;width:290px">
    <h4>MAILING ADDRESS FOR MANAGEMENT</h4>
    <div class="rule"></div>
    <div class="line" style="padding-left:22px;position:relative">
      <svg class="abs" style="left:0;top:5px" width="12" height="14" viewBox="0 0 12 16"><path d="M6 1a4.6 4.6 0 0 0-4.6 4.6C1.4 9.5 6 15 6 15s4.6-5.5 4.6-9.4A4.6 4.6 0 0 0 6 1z" fill="none" stroke="#ddd" stroke-width="1.3"/><circle cx="6" cy="5.7" r="1.6" fill="#ddd"/></svg>
      Lindell Holdings<br>95 Pecan Row, Suite 40<br>Houston, TX 77010
    </div>
  </div>

  <span class="social first" style="left:850px;top:212px" aria-label="Social profile"></span>
  <span class="social" style="left:898px;top:212px" aria-label="Social profile"></span>
  <span class="social" style="left:946px;top:212px" aria-label="Social profile"></span>
  <span class="social" style="left:995px;top:212px" aria-label="Social profile"></span>
</footer>

<p class="copyright">Copyright © BRIGHTDESK Coworking . All Rights Reserved</p>
<span class="pay" style="left:960px;background:#2c4a8c" aria-label="Payment method"></span>
<span class="pay" style="left:1002px;background:#1f3a8a" aria-label="Payment method"></span>
<span class="pay" style="left:1044px;background:#2a2a2a" aria-label="Payment method"></span>
<span class="pay" style="left:1086px;background:#3b7bc4" aria-label="Payment method"></span>
</body>
</html>
```